Building company buisness cards

We are looking for a sharp modern new look for our business cards.
We are a New Zealand based company that specialises in house and land packages.
We have attached a photo of the current logo and would like to see if it can be improved somehow if needed.
We are open to any colours but we have chosen green at this stage.
Feel free to change the font and make the logo smarter looking.
Play with the colours and see what looks best.

We want a card that looks so good know one will want to throw it away!

Target Market(s)

Home buyers

Industry/Entity Type

Building

Contact Information for Business Card

Dorian Keswick
0217392604
dkeswick@tidewellhomecraft.co.nz
tidewellhomecraft.co.nz

Font styles to use
Serif
Sans Serif

Colors

Designer to choose colors to be used in the design.

Requirements
Must have
• Logo and company name on one side, details on the other side
Nice to have
• Color codes for the original green are HEX #4a8028, RGB(74,128,40), CMYK(42,0,69,50)
• Round corners, Raised and/or spot UV

```html
<!DOCTYPE html>
<html lang="en">
<head>
<meta charset="utf-8">
<title>Tidewell Homecraft — Business Cards</title>
<link rel="stylesheet" href="https://fonts.googleapis.com/css2?family=Open+Sans:wght@400;600;700&display=swap">
<style>
  :root {
    --bg: #4a403a;
    --card-dark: #1c1d1f;
    --card-dark-edge: #0f1011;
    --ink-silver: #c9cbcd;
    --card-green: #4a8028;
    --ink-white: #ffffff;
  }
  * { margin: 0; padding: 0; box-sizing: border-box; }
  html, body { width: 1200px; height: 864px; overflow: hidden; }
  body {
    background: var(--bg);
    font-family: "Open Sans", Arial, sans-serif;
    position: relative;
  }
  .card {
    position: absolute;
    width: 520px;
    height: 300px;
    border-radius: 10px;
    box-shadow: 0 14px 30px rgba(0,0,0,0.35);
  }
  /* Front: company name */
  .card--front {
    left: 70px; top: 90px;
    background: var(--card-dark);
    box-shadow: 0 4px 0 var(--card-dark-edge), 0 8px 0 var(--card-dark-edge), 0 18px 34px rgba(0,0,0,0.45);
    display: flex; flex-direction: column; align-items: center; justify-content: center;
    color: var(--ink-silver);
  }
  .brand-name {
    font-weight: 700;
    font-size: 40px;
    line-height: 1.05;
    text-align: center;
    letter-spacing: -0.5px;
  }
  .front-web {
    margin-top: 34px;
    font-size: 15px;
    letter-spacing: 3px;
  }
  /* Back: contact details */
  .card--back {
    left: 610px; top: 474px;
    background: var(--card-green);
    color: var(--ink-white);
    display: flex; align-items: center;
    padding: 0 28px 0 34px;
  }
  .back-brand {
    width: 170px;
    font-weight: 700;
    font-size: 28px;
    line-height: 1.1;
    text-align: center;
  }
  .divider {
    width: 1px; height: 150px;
    background: rgba(255,255,255,0.75);
    margin: 0 22px;
  }
  .contact-name {
    font-weight: 700;
    font-size: 22px;
    text-transform: uppercase;
    letter-spacing: 0.5px;
    margin-bottom: 8px;
  }
  .contact-list { list-style: none; font-size: 13.5px; line-height: 1.55; }
  .contact-list li { display: flex; align-items: center; gap: 8px; }
  .contact-list svg { width: 13px; height: 13px; flex: none; fill: var(--ink-white); }
</style>
</head>
<body>
  <section class="card card--front">
    <div class="brand-name">tidewell<br>homecraft</div>
    <div class="front-web">www.tidewellhomecraft.co.nz</div>
  </section>

  <section class="card card--back">
    <div class="back-brand">tidewell homecraft</div>
    <div class="divider"></div>
    <div class="contact">
      <div class="contact-name">Dorian Keswick</div>
      <ul class="contact-list">
        <li>
          <svg viewBox="0 0 16 16" aria-hidden="true"><path d="M3.5 1.5l2.5 3-1.5 1.5c.8 2 2.5 3.7 4.5 4.5l1.5-1.5 3 2.5-1.5 2.5C7 14 2 9 1 3z"/></svg>
          0217392604
        </li>
        <li>
          <svg viewBox="0 0 16 16" aria-hidden="true"><path d="M1 3h14v10H1z M1.8 3.8L8 8.6l6.2-4.8" stroke="#4a8028" stroke-width="1.2"/></svg>
          dkeswick@tidewellhomecraft.co.nz
        </li>
        <li>
          <svg viewBox="0 0 16 16" aria-hidden="true"><circle cx="8" cy="8" r="7"/><path d="M1 8h14M8 1c-3 3.5-3 10.5 0 14M8 1c3 3.5 3 10.5 0 14" stroke="#4a8028" stroke-width="1" fill="none"/></svg>
          tidewellhomecraft.co.nz
        </li>
      </ul>
    </div>
  </section>
</body>
</html>
```